Wordpress Design Project

The aim of our website is to provide information to a target market of people aged 17 - 22. We need the site to be appealing and also functional that contains a log in and possible forum so people can upload images and ideas. We have broken the information down into four categories and are looking for a website design somewhat like the following. Keeping in mind we are open to feedback from you and also ideas.

Website:
we need a word press design that contains the following:

- 1 main title page that contains a logo at the top centre and 4 main links with the mouse over function.

- all of the four links would then forward you to seperate pages that contain a slide bar at the top which enables the user to view different options. Once the user clicks on the option information will be provided below the scroll system. As well as the information we are looking to have a visual beside it, so a vidplume video beside it.

Target Market(s)

17 - 22 year olds

Industry/Entity Type

Vidplume

Requirements
Nice to have
• Forum and login

```html
<!DOCTYPE html>
<html lang="en">
<head>
<meta charset="utf-8">
<title>Next Step Years</title>
<link href="https://fonts.googleapis.com/css2?family=Montserrat:wght@400;600;700;900&family=Open+Sans:wght@400;600&family=Satisfy&display=swap" rel="stylesheet">
<style>
:root{
  --orange:#ff9c00;
  --orange-light:#ffb400;
  --orange-deep:#ff7e00;
  --black:#151515;
  --dark:#222;
  --red:#e3141f;
  --grey-bg:#f5f5f5;
  --line:#e6e6e6;
  --text:#555;
  --white:#fff;
}
*{margin:0;padding:0;box-sizing:border-box}
html,body{width:984px;height:1200px;overflow:hidden;background:var(--white)}
body{position:relative;font-family:'Open Sans',Arial,sans-serif;color:var(--text)}
.abs{position:absolute}

.topbar{left:0;top:0;width:984px;height:30px;background:linear-gradient(#fff,#ececec)}
.btn-small{top:5px;height:21px;border-radius:3px;color:#fff;font:600 11px 'Montserrat',sans-serif;display:flex;align-items:center;gap:5px;padding:0 8px}
.btn-register{left:725px;background:var(--black)}
.btn-login{left:815px;background:var(--red)}

.mainnav{left:0;top:30px;width:984px;height:42px;background:var(--black);border-bottom:1px solid #444}
.mainnav a{position:absolute;top:14px;color:#fff;font:700 12px 'Montserrat',sans-serif;text-decoration:none}

.brand-tab{left:428px;top:0;width:128px;height:110px;z-index:5}
.brand-name{left:428px;top:12px;width:128px;text-align:center;color:#fff;font:900 34px/1 'Montserrat',sans-serif;letter-spacing:-1px;z-index:6}
.brand-sub{left:428px;top:52px;width:128px;text-align:center;color:#fff;font:900 10px 'Montserrat',sans-serif;z-index:6}

.hero{left:0;top:72px;width:984px;height:451px;background:linear-gradient(100deg,#6f8a3a 0%,#a8b86a 30%,#5d7a2e 55%,#8ba64e 80%,#4f6a22 100%)}
.hero-person{left:115px;top:84px;width:395px;height:439px;background:linear-gradient(180deg,#3a2f2a 0%,#d9b59e 30%,#a05a4a 65%,#e9e4dc 100%);border-radius:180px 180px 0 0;opacity:.85}

.login-panel{left:509px;top:152px;width:362px;height:157px;background:rgba(255,255,255,.55);border:1px solid rgba(255,255,255,.7);border-radius:4px;overflow:hidden}
.login-head{height:43px;background:var(--dark);color:#fff;font:700 18px/43px 'Montserrat',sans-serif;padding-left:16px}
.field{position:absolute;top:67px;width:160px;height:28px;background:#fff;border:1px solid #bbb;font-size:11px;line-height:26px;padding-left:10px;color:#555}
.login-btn{left:16px;top:108px;width:87px;height:31px;background:var(--red);border-radius:3px;color:#fff;font:700 15px 'Montserrat',sans-serif;display:flex;align-items:center;justify-content:center;gap:7px}
.forgot{left:186px;top:104px;font-size:10px;color:#222}
.hero-copy{left:518px;top:328px;width:360px;color:#fff;font:600 12px/18.5px 'Montserrat',sans-serif}
.hero-copy span{color:var(--orange)}

.register-cta{left:357px;top:502px;width:271px;height:49px;background:linear-gradient(var(--orange-light),var(--orange-deep));border-radius:3px;color:#fff;font:900 22px 'Montserrat',sans-serif;display:flex;align-items:center;justify-content:center;gap:10px;box-shadow:0 3px 6px rgba(0,0,0,.2)}

.welcome-rule{top:601px;height:4px;background:var(--line)}
.welcome-script{left:0;top:576px;width:984px;text-align:center;font:24px 'Satisfy',cursive;color:#333}
.welcome-title{left:0;top:602px;width:984px;text-align:center;font:400 21px 'Montserrat',sans-serif;color:var(--orange)}
.welcome-text{left:118px;top:637px;width:748px;text-align:center;font-size:10.5px;line-height:17.7px;color:#555}
.welcome-text p+p{margin-top:18px}

.feature-band{left:0;top:787px;width:984px;height:285px;background:var(--grey-bg)}
.section-title{font:400 19px 'Montserrat',sans-serif;color:var(--orange)}
.section-title em{font:22px 'Satisfy',cursive;color:#222;font-style:normal;margin-right:4px}
.video-frame{left:107px;top:847px;width:240px;height:181px;background:#fff;border:1px solid #ddd;padding:4px}
.video-still{width:100%;height:150px;background:linear-gradient(90deg,#3b3a36,#7a6a55 50%,#4a4e44)}
.video-bar{height:22px;background:#1b1b1b;position:relative;color:#ddd;font-size:8px}
.upload-label{font-size:10.5px;color:#555}
.file-input{left:384px;top:887px;width:166px;height:16px;background:#fff;border:1px solid #bbb}
.browse{left:551px;top:886px;width:53px;height:17px;background:linear-gradient(#f5f5f5,#ddd);border:1px solid #999;font-size:10px;color:#222;text-align:center;line-height:15px}
.desc-box{left:384px;top:933px;width:219px;height:101px;background:#fff;border:1px solid #ddd}
.images-box{left:633px;top:876px;width:242px;height:94px;background:#fff;border:2px solid #e3e3e3;text-align:center;line-height:90px;font-size:14px;color:#333}
.upload-btn{left:633px;top:984px;width:242px;height:50px;background:linear-gradient(#333,#111);border-radius:4px;color:#fff;font:900 23px 'Montserrat',sans-serif;display:flex;align-items:center;justify-content:center;gap:10px}

.contact-band{left:0;top:1072px;width:984px;height:89px;background:var(--orange-light)}
.contact{position:absolute;top:18px;color:#fff;display:flex;gap:10px}
.contact h4{font:600 14px 'Montserrat',sans-serif}
.contact p{font:600 10px/14px 'Montserrat',sans-serif}

.footer{left:0;top:1161px;width:984px;height:39px;background:var(--black)}
.copyright{left:107px;top:13px;color:#ccc;font:400 10px 'Montserrat',sans-serif}
.social{position:absolute;top:9px;width:20px;height:20px;border-radius:2px}
</style>
</head>
<body>

<div class="abs topbar"></div>
<div class="abs btn-small btn-register">
  <svg width="10" height="10" viewBox="0 0 10 10"><path d="M1 9l1-3 5-5 2 2-5 5z" fill="#fff"/></svg>REGISTER
</div>
<div class="abs btn-small btn-login">
  <svg width="9" height="10" viewBox="0 0 9 10"><rect x="0" y="4" width="9" height="6" fill="#fff"/><path d="M2 4V3a2.5 2.5 0 015 0v1" stroke="#fff" stroke-width="1.5" fill="none"/></svg>LOGIN
</div>

<nav class="abs mainnav">
  <a style="left:184px">GAP YEAR</a>
  <a style="left:303px">SCHOOLIES</a>
  <a style="left:613px">UNIVERSITY</a>
  <a style="left:743px">TRADES</a>
</nav>

<section class="abs hero" role="img" aria-label="Outdoor photo backdrop of blurred green trees"></section>
<div class="abs hero-person" role="img" aria-label="Photo of a smiling student holding a pen and notebook"></div>

<svg class="abs brand-tab" viewBox="0 0 128 110"><path d="M0 0H128V82L64 110 0 82Z" fill="var(--orange)"/></svg>
<div class="abs brand-name">NEXT</div>
<div class="abs brand-sub">STEP YEARS</div>

<div class="abs login-panel">
  <div class="login-head">USER LOGIN</div>
  <div class="field" style="left:16px">User Name :</div>
  <div class="field" style="left:187px">Password :</div>
  <div class="abs login-btn">
    <svg width="12" height="14" viewBox="0 0 12 14"><rect x="0" y="6" width="12" height="8" fill="#fff"/><path d="M3 6V4a3 3 0 016 0v2" stroke="#fff" stroke-width="2" fill="none"/></svg>LOGIN
  </div>
  <div class="abs forgot">Forgot your password?</div>
</div>

<p class="abs hero-copy">This is Draftloom's version of Lorem Ipsum. Proin gravida nibh vel velit auctor aliquet. Aenean sollicitudin, lorem quis bibendum auctor, nisi elit consequat ipsum, nec sagittis sem nibh id elit. Duis sed odio sit amet nibh vulputate cursus a sit amet mauris. <span>[Read More...]</span></p>

<div class="abs register-cta">
  <svg width="22" height="22" viewBox="0 0 22 22"><rect x="2" y="4" width="16" height="16" rx="2" fill="none" stroke="#fff" stroke-width="2.5"/><path d="M8 14l1-4 9-9 3 3-9 9z" fill="#fff"/></svg>REGISTER NOW!
</div>

<div class="abs welcome-rule" style="left:107px;width:254px"></div>
<div class="abs welcome-rule" style="left:624px;width:253px"></div>
<div class="abs welcome-script">Welcome to</div>
<h1 class="abs welcome-title">NEXT STEP YEARS</h1>
<div class="abs welcome-text">
  <p>This is Draftloom's version of Lorem Ipsum. Proin gravida nibh vel velit auctor aliquet. Aenean sollicitudin, lorem quis bibendum auctor, nisi elit consequat ipsum, nec sagittis sem nibh id elit. Duis sed odio sit amet nibh vulputate cursus a sit amet mauris. Morbi accumsan ipsum velit. Nam nec tellus a odio tincidunt auctor a ornare odio. Sed non mauris vitae erat consequat auctor eu in elit. Class aptent taciti sociosqu ad litora torquent per conubia nostra, per inceptos himenaeos.</p>
  <p>Mauris in erat justo. Nullam ac urna eu felis dapibus condimentum sit amet a augue. Sed non neque elit. Sed ut imperdiet nisi. Proin condimentum fermentum nunc. Etiam pharetra, erat sed fermentum feugiat, velit mauris egestas quam, ut aliquam massa nisl quis neque.</p>
</div>

<section class="abs feature-band"></section>
<h2 class="abs section-title" style="left:107px;top:812px"><em>Latest</em>VIDEO</h2>
<div class="abs video-frame">
  <div class="video-still" role="img" aria-label="Video still of a student reading outdoors" style="position:relative">
    <svg style="position:absolute;left:97px;top:54px" width="42" height="42" viewBox="0 0 42 42"><circle cx="21" cy="21" r="19" fill="rgba(0,0,0,.3)" stroke="#fff" stroke-width="2.5"/><path d="M16 12l13 9-13 9z" fill="#fff"/></svg>
  </div>
  <div class="video-bar">
    <div style="position:absolute;left:0;top:0;width:100%;height:3px;background:#555"></div>
    <div style="position:absolute;left:0;top:0;width:36px;height:3px;background:#c00"></div>
    <svg style="position:absolute;left:8px;top:9px" width="9" height="9" viewBox="0 0 9 9"><path d="M0 0l9 4.5L0 9z" fill="#ddd"/></svg>
    <span style="position:absolute;left:70px;top:8px">0:14 / 2:57</span>
    <span style="position:absolute;left:160px;top:8px">360p</span>
  </div>
</div>

<h2 class="abs section-title" style="left:384px;top:812px"><em>Upload Your</em>INNOVATION</h2>
<div class="abs" style="left:384px;top:847px;width:491px;height:4px;background:var(--line)"></div>
<div class="abs upload-label" style="left:384px;top:867px">Select Your File</div>
<div class="abs file-input"></div>
<div class="abs browse">Browse</div>
<div class="abs upload-label" style="left:384px;top:915px">Description</div>
<div class="abs desc-box"></div>
<div class="abs images-box">Images</div>
<div class="abs upload-btn">
  <svg width="22" height="22" viewBox="0 0 22 22"><path d="M11 2l7 7h-4v6H8V9H4z" fill="#fff"/><path d="M2 14v6h18v-6" stroke="#fff" stroke-width="2.5" fill="none"/></svg>UPLOAD NOW!
</div>

<footer class="abs contact-band">
  <div class="contact" style="left:107px">
    <svg width="16" height="24" viewBox="0 0 16 24"><path d="M8 0a8 8 0 00-8 8c0 6 8 16 8 16s8-10 8-16a8 8 0 00-8-8z" fill="#fff"/><circle cx="8" cy="8" r="3" fill="var(--orange-light)"/></svg>
    <div><h4>Location</h4><p>22, Stress address,<br>Cityname, 886 Country.</p></div>
  </div>
  <div class="contact" style="left:302px">
    <svg width="16" height="26" viewBox="0 0 16 26"><rect width="16" height="26" rx="3" fill="#fff"/><rect x="3" y="4" width="10" height="15" fill="var(--orange-light)"/></svg>
    <div><h4>Phone :</h4><p>(800) 21 604 73150</p></div>
  </div>
  <div class="contact" style="left:484px">
    <svg width="26" height="18" viewBox="0 0 26 18"><rect width="26" height="18" fill="#fff"/><path d="M0 0l13 10L26 0" stroke="var(--orange-light)" stroke-width="2" fill="none"/></svg>
    <div><h4>Email :</h4><p>hello@nextstepmail.com</p></div>
  </div>
  <div class="contact" style="left:685px">
    <svg width="24" height="22" viewBox="0 0 24 22"><rect width="24" height="16" rx="1" fill="#fff"/><rect x="2" y="2" width="20" height="12" fill="var(--orange-light)"/><rect x="8" y="18" width="8" height="3" fill="#fff"/></svg>
    <div><h4>Website :</h4><p>www.nextstepyears.com.au</p></div>
  </div>
</footer>

<div class="abs footer">
  <div class="abs copyright">Copyright ©2013 nextstepyears.com.au. All Rights Reserved.</div>
  <span class="social" style="left:727px;background:#3b5998" aria-label="Social link"></span>
  <span class="social" style="left:753px;background:#2aa9e0" aria-label="Social link"></span>
  <span class="social" style="left:779px;background:#0e76a8" aria-label="Social link"></span>
  <span class="social" style="left:805px;background:#dd4b39" aria-label="Social link"></span>
  <span class="social" style="left:831px;background:#12a5f4" aria-label="Social link"></span>
  <span class="social" style="left:857px;background:#c4302b" aria-label="Vidplume"></span>
</div>

</body>
</html>
```